Fernwick

We require a professional design for a Cosmetic Surgery college. We have just submitted the request for our new logo which will be used on this card. We are the leaders in our field of education in Australia and this should be reflected in the quality of the card. People want to come and study with us because we are so outstanding in the field. Studying with us provides credibility, quality and courage.
Updates

Project Deadline Extended
Reason: Require updated logo to be used in design

Target Market(s)

25 - 40 year old professional women primarily from a medical background wanting to continue study in the cosmetic medical field, western speaking countries. The course average cost is 17k AU for 16 weeks.

Industry/Entity Type

Education

Requirements
Must have
• Must us the logo that is currently under design by this company.
Nice to have
• A medical twist very subtle would be nice possilbly rod of Asclepius.
Should not have
• Should not look old, we are dealing with modern medical concepts.
The logo that is being redesigned 3d silver, the attached logo is the old one.

```html
<!DOCTYPE html>
<html lang="en">
<head>
<meta charset="utf-8">
<title>Fernwick – Business Card</title>
<link rel="stylesheet" href="https://fonts.googleapis.com/css2?family=Open+Sans:wght@300;400;600&family=Cinzel:wght@400&display=swap">
<style>
  :root {
    --page-bg: #e9e6e1;
    --card-dark: #0b0c0d;
    --card-mid: #2a2c2f;
    --silver: #d6d8da;
    --silver-soft: #a9adb1;
    --accent-blue: #31b4cf;
    --text-light: #eef0f1;
    --icon-bg: #3a5f8f;
  }
  * { box-sizing: border-box; margin: 0; padding: 0; }
  html, body {
    width: 1200px; height: 1023px; overflow: hidden;
    background: var(--page-bg);
    font-family: "Open Sans", Arial, sans-serif;
  }
  .stage { position: relative; width: 1200px; height: 1023px; }

  .card {
    position: absolute;
    width: 600px; height: 343px;
    border-radius: 6px;
    background: linear-gradient(135deg, var(--card-mid) 0%, var(--card-dark) 55%, #000 100%);
    box-shadow: 0 14px 30px rgba(0,0,0,0.28);
    overflow: hidden;
    color: var(--text-light);
  }
  .card--front { left: 70px; top: 100px; }
  .card--back  { left: 530px; top: 580px; }

  .swoosh { position: absolute; inset: 0; width: 100%; height: 100%; }

  .brand { position: absolute; display: flex; align-items: center; gap: 12px; white-space: nowrap; }
  .brand__dot {
    width: 56px; height: 56px; border-radius: 50%;
    background: radial-gradient(circle at 35% 30%, #ffffff 0%, var(--silver) 40%, var(--silver-soft) 100%);
    flex: none;
  }
  .brand__text { display: flex; flex-direction: column; }
  .brand__name {
    font-weight: 300; font-size: 36px; letter-spacing: 2.5px; line-height: 1;
    color: var(--silver);
  }
  .brand__tagline {
    font-weight: 300; font-size: 7.4px; letter-spacing: 0.3px;
    color: var(--silver); margin-top: 5px; text-transform: uppercase;
  }
  .card--front .brand { left: 34px; top: 74px; }
  .card--back .brand { left: 50%; top: 50%; transform: translate(-50%, -50%); }
  .card--back .brand__name { font-size: 58px; letter-spacing: 3px; }
  .card--back .brand__dot { width: 74px; height: 74px; }
  .card--back .brand__tagline { font-size: 11.5px; letter-spacing: 0.5px; }

  .person { position: absolute; left: 102px; top: 158px; white-space: nowrap; }
  .person__name {
    font-family: "Cinzel", Georgia, serif; font-size: 19px; letter-spacing: 1.2px;
    color: var(--text-light);
  }
  .person__role { font-size: 9.5px; letter-spacing: 1px; margin-top: 3px; text-transform: uppercase; color: var(--silver-soft); }

  .contact {
    position: absolute; right: 26px; top: 150px;
    list-style: none; text-align: right;
  }
  .contact li {
    display: flex; justify-content: flex-end; align-items: center; gap: 10px;
    font-size: 13px; line-height: 22px; color: var(--text-light); white-space: nowrap;
  }
  .contact__icon {
    width: 13px; height: 13px; border-radius: 2px; flex: none;
    background: var(--icon-bg); display: inline-flex; align-items: center; justify-content: center;
  }
  .contact__icon svg { width: 9px; height: 9px; }

  .address {
    position: absolute; right: 26px; bottom: 20px;
    text-align: right; font-weight: 600; font-size: 11px; letter-spacing: 0.2px;
    color: var(--accent-blue); text-transform: uppercase; white-space: nowrap;
  }
</style>
</head>
<body>
<main class="stage">

  <section class="card card--front" aria-label="Business card front">
    <svg class="swoosh" viewBox="0 0 600 343" aria-hidden="true">
      <path d="M462 0 C 392 80, 318 200, 274 343" fill="none" stroke="#c9ccd0" stroke-width="2.5"/>
      <path d="M476 0 C 406 80, 332 200, 290 343 L 278 343 C 322 200, 396 80, 466 0 Z" fill="var(--accent-blue)"/>
    </svg>

    <div class="brand">
      <span class="brand__dot"></span>
      <div class="brand__text">
        <span class="brand__name">FERNWICK</span>
        <span class="brand__tagline">Medical and Cosmetic Aesthetics Education</span>
      </div>
    </div>

    <div class="person">
      <p class="person__name">MARA ELLISON</p>
      <p class="person__role">Director</p>
    </div>

    <ul class="contact">
      <li>1300 482 517
        <span class="contact__icon"><svg viewBox="0 0 10 10"><path d="M2 1h2l1 2-1 1a5 5 0 0 0 2 2l1-1 2 1v2c-4 0-7-3-7-7z" fill="#fff"/></svg></span></li>
      <li>0402 318 745
        <span class="contact__icon"><svg viewBox="0 0 10 10"><rect x="3" y="1" width="4" height="8" rx="1" fill="#fff"/></svg></span></li>
      <li>hello@fernwick.edu.au
        <span class="contact__icon"><svg viewBox="0 0 10 10"><rect x="1" y="2.5" width="8" height="5" fill="#fff"/><path d="M1 2.5l4 3 4-3" fill="none" stroke="#3a5f8f"/></svg></span></li>
      <li>www.fernwick.edu.au/campus
        <span class="contact__icon"><svg viewBox="0 0 10 10"><circle cx="5" cy="5" r="3.6" fill="none" stroke="#fff"/><path d="M1.5 5h7M5 1.4v7.2" stroke="#fff"/></svg></span></li>
    </ul>

    <p class="address">48 Harbour Ln, Southport QLD 4215</p>
  </section>

  <section class="card card--back" aria-label="Business card back">
    <div class="brand">
      <span class="brand__dot"></span>
      <div class="brand__text">
        <span class="brand__name">FERNWICK</span>
        <span class="brand__tagline">Medical and Cosmetic Aesthetics Education</span>
      </div>
    </div>
  </section>

</main>
</body>
</html>
```